Climb the Marlow

Need a Postcard for Lumen Harbor Card Service Campaign that is flexible and dates and times can be changed as needed. create an invitation section.."You're Invited" to a workshop...Time, Date, Place is what needs to be changeable on the Korvel Lantis version for us to log in and order on an as needed basis. Will this be loaded onto our Korvel Lantis Account to change the info as we mail? Must be formatted properly for Lumen Harbor Card Service in United States. Postcard size will be 9" Wide X 6" high. The focus is on the word MARLOW....

```html
<!DOCTYPE html>
<html lang="en">
<head>
<meta charset="utf-8">
<title>Climb the Marlow – Workshop Postcard Back</title>
<link rel="stylesheet" href="https://fonts.googleapis.com/css2?family=Roboto+Condensed:wght@400;700&family=Damion&display=swap">
<style>
  :root {
    --page-bg: #3a3a3a;
    --card-white: #ffffff;
    --sky-top: #9fdbe6;
    --sky-mid: #d7f0f4;
    --ink-grey: #4f5256;
    --brand-blue: #1f4582;
    --panel-blue: #1c4380;
    --bracket-grey: #d3d5d8;
    --line-black: #111111;
  }
  * { margin: 0; padding: 0; box-sizing: border-box; }
  html, body { width: 1200px; height: 927px; overflow: hidden; }
  body {
    background: var(--page-bg);
    position: relative;
    font-family: "Roboto Condensed", "Arial Narrow", sans-serif;
  }
  .postcard {
    position: absolute;
    left: 109px; top: 76px;
    width: 982px; height: 681px;
    background: var(--card-white);
    overflow: hidden;
  }
  .sky-backdrop {
    position: absolute;
    left: 0; top: 0; width: 100%; height: 320px;
    background:
      radial-gradient(ellipse 260px 60px at 120px 20px, rgba(255,255,255,0.7), rgba(255,255,255,0) 70%),
      radial-gradient(ellipse 300px 80px at 420px 60px, rgba(255,255,255,0.6), rgba(255,255,255,0) 70%),
      linear-gradient(180deg, var(--sky-top) 0%, var(--sky-mid) 30%, rgba(255,255,255,0) 100%),
      linear-gradient(90deg, rgba(159,219,230,0.6) 0%, rgba(255,255,255,0) 85%);
  }
  .intro-heading {
    position: absolute;
    left: 30px; top: 56px; width: 500px;
    text-align: center;
    font-weight: 700; font-size: 17px; line-height: 20px;
    color: var(--ink-grey);
  }
  .question-list { list-style: none; }
  .question {
    position: absolute;
    width: 240px;
    font-size: 14px; line-height: 18px;
    color: var(--ink-grey);
    padding-left: 13px;
  }
  .question::before {
    content: "";
    position: absolute; left: 0; top: 4px;
    border-left: 6px solid var(--ink-grey);
    border-top: 5px solid transparent;
    border-bottom: 5px solid transparent;
  }
  .q-debt-free { left: 39px; top: 128px; }
  .q-job-free { left: 291px; top: 128px; }
  .q-secure { left: 39px; top: 216px; }
  .q-bank { left: 291px; top: 216px; }
  .offer-text {
    position: absolute;
    left: 20px; top: 308px; width: 520px;
    text-align: center;
    font-size: 17px; line-height: 20px;
    color: var(--ink-grey);
  }
  .offer-url {
    position: absolute;
    left: 20px; top: 349px; width: 520px;
    text-align: center;
    font-size: 27px; color: var(--brand-blue);
  }
  .offer-url strong { font-weight: 700; }
  .bracket { position: absolute; width: 32px; height: 32px; border-color: var(--bracket-grey); border-style: solid; }
  .bracket-top-left { left: 32px; top: 406px; border-width: 4px 0 0 4px; }
  .bracket-bottom-right { left: 500px; top: 544px; border-width: 0 4px 4px 0; }
  .invite-panel {
    position: absolute;
    left: 42px; top: 416px; width: 480px; height: 150px;
    background: var(--panel-blue);
    color: #fff;
  }
  .invite-title {
    position: absolute; left: 18px; top: 4px;
    font-family: "Damion", cursive;
    font-weight: 400; font-size: 46px; line-height: 44px;
  }
  .invite-title .line-two { display: block; padding-left: 38px; }
  .invite-subtitle {
    position: absolute; left: 92px; top: 112px;
    font-size: 20px;
  }
  .event-details { position: absolute; left: 249px; top: 16px; width: 216px; }
  .event-heading {
    font-weight: 400; font-size: 22px; line-height: 26px;
    padding-bottom: 7px; border-bottom: 2px solid #fff; margin-bottom: 6px;
  }
  .event-row { display: flex; font-size: 21px; line-height: 25px; padding-left: 3px; }
  .event-label { width: 60px; }
  .event-colon { width: 22px; }
  .rsvp-line {
    position: absolute; left: 20px; top: 594px; width: 520px;
    text-align: center;
    font-weight: 700; font-size: 26px; color: var(--brand-blue);
  }
  .postage-indicia {
    position: absolute; left: 852px; top: 49px; width: 81px; height: 80px;
    border: 2px solid var(--line-black);
    font-family: Arial, Helvetica, sans-serif;
    font-size: 10.5px; line-height: 12px; text-align: center;
    padding-top: 6px; color: var(--line-black);
  }
  .address-block {
    position: absolute; left: 602px; top: 197px; width: 233px; height: 64px;
    border: 2px solid var(--line-black);
    font-family: Arial, Helvetica, sans-serif;
    font-size: 12px; line-height: 14px;
    padding: 7px 0 0 7px; color: var(--line-black);
  }
</style>
</head>
<body>
  <main class="postcard">
    <div class="sky-backdrop" role="img" aria-label="Soft blue sky with light clouds"></div>

    <h1 class="intro-heading">If you feel you haven’t saved enough, you won’t ever be able to retire and are worried about your future and retirement dreams, then maybe it’s time to start asking different questions:</h1>

    <ul class="question-list">
      <li class="question q-debt-free">If all of my debts were paid, and most of my income was tax-free, how much money would I need to simply enjoy my life?</li>
      <li class="question q-job-free">If I am debt free years before I am “job free,” can I choose a job that better fits my dreams and goals and do what I’ve always dreamed of doing?</li>
      <li class="question q-secure">If I can’t retire because I haven’t saved enough, what CAN I do to make my financial life feel more secure?</li>
      <li class="question q-bank">If I never needed to beg a bank to lend me more money again, would I feel liberated from the rat race?</li>
    </ul>

    <p class="offer-text">Let us help you take a different, and we believe better, approach to planning your retirement.For your FREE report, go to:</p>
    <p class="offer-url">www.<strong>ClimbTheMarlow</strong>.com</p>

    <span class="bracket bracket-top-left"></span>
    <span class="bracket bracket-bottom-right"></span>
    <section class="invite-panel">
      <h2 class="invite-title">You’re<span class="line-two">Invited</span></h2>
      <p class="invite-subtitle">to a workshop...</p>
      <div class="event-details">
        <h3 class="event-heading">Join Us to Learn More!</h3>
        <p class="event-row"><span class="event-label">Time</span><span class="event-colon">:</span><span class="event-value">00:00 to 00:00</span></p>
        <p class="event-row"><span class="event-label">Date</span><span class="event-colon">:</span><span class="event-value">00/00/0000</span></p>
        <p class="event-row"><span class="event-label">Place</span><span class="event-colon">:</span><span class="event-value">Lorem Ipsum</span></p>
      </div>
    </section>

    <p class="rsvp-line">RSVP to 1-555-014-2290 Ext. 315</p>

    <div class="postage-indicia">PRSRT STD<br>ECRWSS<br>U.S. POSTAGE<br>PAID<br>LHCS RETAIL</div>
    <div class="address-block">Local<br>Postal Customer</div>
  </main>
</body>
</html>
```